Realty Group Needs Classy, Contemporary Letterhead Design

We need a letterhead design for a new realty company located in NY, USA. We buy investment properties to rehabilitate and or keep in our rental portfolio.

```html
<!DOCTYPE html>
<html lang="en">
<head>
<meta charset="utf-8">
<title>Meridian Realty Group – Letterhead</title>
<link href="https://fonts.googleapis.com/css2?family=Montserrat:wght@800&family=Roboto:wght@500&display=swap" rel="stylesheet">
<style>
  :root {
    --backdrop: #e6e6e6;
    --paper: #ffffff;
    --brand-purple: #4f2d84;
    --accent-grey: #7f7f7f;
    --wash-light: #f8f8fb;
    --wash-deep: #efedf6;
    --footer-text: #ffffff;
  }
  html, body {
    margin: 0;
    padding: 0;
    width: 1023px;
    height: 1200px;
    overflow: hidden;
    background: var(--backdrop);
  }
  .letterhead {
    position: absolute;
    left: 87px;
    top: 0;
    width: 849px;
    height: 1200px;
    background: var(--paper);
    overflow: hidden;
  }
  .letterhead__art {
    position: absolute;
    inset: 0;
    width: 849px;
    height: 1200px;
  }
  .brand-name {
    position: absolute;
    right: 67px;
    top: 92px;
    margin: 0;
    font-family: "Montserrat", sans-serif;
    font-weight: 800;
    font-size: 22px;
    letter-spacing: 0.2px;
    color: var(--brand-purple);
    white-space: nowrap;
  }
  .contact-list {
    position: absolute;
    left: 45px;
    top: 1097px;
    margin: 0;
    padding: 0;
    list-style: none;
    font-family: "Roboto", sans-serif;
    font-weight: 500;
    font-size: 13px;
    color: var(--footer-text);
  }
  .contact-list__item {
    display: flex;
    align-items: center;
    height: 26.5px;
  }
  .contact-list__icon {
    width: 15px;
    height: 15px;
    margin-right: 10px;
    fill: var(--footer-text);
  }
</style>
</head>
<body>
  <div class="letterhead">
    <svg class="letterhead__art" viewBox="0 0 849 1200" xmlns="http://www.w3.org/2000/svg">
      <defs>
        <linearGradient id="wash" x1="0" y1="0" x2="1" y2="0">
          <stop offset="0" stop-color="var(--wash-light)"/>
          <stop offset="1" stop-color="var(--wash-deep)"/>
        </linearGradient>
      </defs>
      <!-- top corner accents -->
      <polygon class="corner-grey" points="0,0 131,0 0,34" fill="var(--accent-grey)"/>
      <polygon class="header-band" points="241,0 849,0 849,31 120,31" fill="var(--brand-purple)"/>
      <!-- faint background emblem area -->
      <polygon class="background-wash" role="img" aria-label="Faint oversized brand emblem in the lower page background"
               points="0,708 849,708 849,961 729,1076 0,1076" fill="url(#wash)"/>
      <!-- footer -->
      <polygon class="footer-band" points="0,1076 729,1076 611,1200 0,1200" fill="var(--brand-purple)"/>
      <polygon class="corner-grey" points="849,1068 849,1200 717,1200" fill="var(--accent-grey)"/>
    </svg>

    <p class="brand-name">Meridian Realty Group, LLC</p>

    <ul class="contact-list">
      <li class="contact-list__item">
        <svg class="contact-list__icon" viewBox="0 0 24 24"><path d="M12 2a7 7 0 0 0-7 7c0 5 7 13 7 13s7-8 7-13a7 7 0 0 0-7-7zm0 9.5A2.5 2.5 0 1 1 12 6.5a2.5 2.5 0 0 1 0 5z"/></svg>
        0123 Zip,abc City
      </li>
      <li class="contact-list__item">
        <svg class="contact-list__icon" viewBox="0 0 24 24"><path d="M6.6 10.8a15.1 15.1 0 0 0 6.6 6.6l2.2-2.2a1 1 0 0 1 1-.25 11.4 11.4 0 0 0 3.6.57 1 1 0 0 1 1 1V20a1 1 0 0 1-1 1A17 17 0 0 1 3 4a1 1 0 0 1 1-1h3.5a1 1 0 0 1 1 1c0 1.25.2 2.45.57 3.57a1 1 0 0 1-.25 1z"/></svg>
        +00 1234 56 789
      </li>
      <li class="contact-list__item">
        <svg class="contact-list__icon" viewBox="0 0 24 24"><path d="M22 2 2 10.5l7 2.5 2.5 7L22 2zM9.8 12.2l8-6.4-6.2 8z"/></svg>
        info@company.com
      </li>
    </ul>
  </div>
</body>
</html>
```